Print materials for 3-star hotel

We are changing up our print materials (notepads, letterheads, key card jackets, small flyer for the room rates) We are a 3 star business hotel in the Philippines and have mainly used grey tones and clean, simple lines. See attached photos for logo and hotel interior photos.

Target Market(s)

Business

Contact Information for Business Card

Tamarind Crest Hotel
Governor Lualhati Avenue corner Pindang St Cebu City 6000 Philippines
Tel: +63 32 480 5273
Mobile: +63 917 608 4926
www.tamarindcresthotel.example

Font styles to use
Serif
Sans Serif

Requirements
Must have
• Simple
• Readable font and font size
Nice to have
• Neutral colors, grey and taupes
Should not have
• No purples and bright blues

```html
<!DOCTYPE html>
<html lang="en">
<head>
<meta charset="utf-8">
<title>Tamarind Crest Hotel – Stationery</title>
<link rel="stylesheet" href="https://fonts.googleapis.com/css2?family=Cinzel:wght@400&family=Montserrat:wght@400;600;700&display=swap">
<style>
:root{
  --backdrop:#a9a9a9;
  --paper:#f1f1f1;
  --paper-edge:#e2e2e2;
  --taupe:#4b4038;
  --sheet-grey:#8e8e8e;
  --cover-grey:#868686;
  --cover-dark:#5d5d5d;
  --ink:#6a6a6a;
  --ink-strong:#4d4d4d;
  --on-dark:#f3f1ee;
}
*{margin:0;padding:0;box-sizing:border-box}
html,body{width:1200px;height:1132px;overflow:hidden;background:var(--backdrop)}
.canvas{position:relative;width:1200px;height:1132px;font-family:"Montserrat",sans-serif;color:var(--ink)}
.piece{position:absolute}

/* wordmark */
.wordmark{font-family:"Cinzel",serif;font-weight:400;text-align:center;color:var(--taupe);line-height:1.15;letter-spacing:.12em}
.wordmark .name{display:block}
.wordmark .sub{display:block;letter-spacing:.3em}

/* letterhead */
.backing-sheet{left:102px;top:208px;width:460px;height:650px;background:var(--sheet-grey)}
.letterhead{left:44px;top:132px;width:460px;height:650px;background:var(--paper)}
.letterhead .wordmark{position:absolute;left:30px;top:40px;width:180px;font-size:13px}
.letterhead .wordmark .sub{font-size:9px}
.contact-block{position:absolute;right:40px;top:36px;text-align:right;font-size:6.6px;line-height:10.5px;color:var(--ink)}
.contact-block b{font-weight:700}
.contact-block .phones{margin-top:5px}
.phone-row{display:flex;justify-content:flex-end;align-items:center;gap:4px}
.phone-row svg{width:7px;height:7px}
.letter-body{position:absolute;left:42px;top:186px;width:380px;font-size:6.6px;line-height:14px;color:var(--ink);text-align:justify}
.letter-body p{margin-bottom:14px}
.letter-body .signer{font-weight:700;color:var(--ink-strong);margin-bottom:18px}
.signature-line{display:block;width:120px;height:14px}
.letter-footer{position:absolute;left:0;right:0;top:617px;text-align:center;font-size:7px;font-weight:600;color:var(--ink)}
.letter-footer span{margin:0 8px}

/* envelopes */
.envelope-front{left:602px;top:124px;width:434px;height:226px;background:var(--paper)}
.envelope-front svg.flap{position:absolute;left:0;top:0;width:434px;height:82px}
.envelope-front .wordmark{position:absolute;left:0;right:0;top:150px;font-size:12px}
.envelope-front .wordmark .sub{font-size:8.5px}
.envelope-back{left:704px;top:390px;width:458px;height:228px;background:var(--paper)}
.envelope-back .contact-left{position:absolute;left:26px;top:144px;font-size:6.6px;line-height:10px}
.envelope-back .contact-left b{font-weight:700}
.envelope-back .phones{margin-top:3px}
.envelope-back .phone-row{justify-content:flex-start}
.envelope-back .contact-right{position:absolute;right:24px;top:190px;text-align:right;font-size:6.6px;line-height:10px}

/* business cards */
.card-front{left:214px;top:886px;width:240px;height:133px;background:var(--paper)}
.card-front .holder{position:absolute;left:18px;top:26px;font-size:8px;font-weight:700;color:var(--ink-strong)}
.card-front .role{position:absolute;left:18px;top:37px;font-size:5px;color:var(--ink)}
.card-front .rule{position:absolute;left:18px;top:58px;width:14px;height:1px;background:var(--ink)}
.card-front .mini-mark{position:absolute;right:18px;top:24px;font-family:"Cinzel",serif;font-size:7px;color:var(--taupe);letter-spacing:.1em;text-align:right;line-height:1.2}
.card-front .lines{position:absolute;left:18px;top:74px;font-size:5px;line-height:8.6px}
.card-front .lines .phone-row{justify-content:flex-start}
.card-front .lines svg{width:5.5px;height:5.5px}
.card-front .address{position:absolute;right:18px;top:85px;text-align:right;font-size:5px;line-height:8.6px}
.card-front .address b{font-weight:700}
.card-back{left:476px;top:886px;width:240px;height:133px;background:var(--taupe)}
.card-back .wordmark{position:absolute;left:0;right:0;top:50px;color:var(--on-dark);font-size:11.5px}
.card-back .wordmark .sub{font-size:8px}

/* notebook */
.notebook{left:752px;top:666px;width:266px;height:380px;background:var(--cover-grey);border-radius:0 12px 12px 0;overflow:hidden}
.notebook .spine{position:absolute;left:0;top:0;width:22px;height:100%;background:var(--cover-dark)}
.notebook .strap{position:absolute;left:206px;top:0;width:11px;height:100%;background:var(--cover-dark)}
.notebook .wordmark{position:absolute;left:22px;width:184px;top:168px;color:var(--on-dark);font-size:11px}
.notebook .wordmark .sub{font-size:8px}
</style>
</head>
<body>
<div class="canvas">

  <svg width="0" height="0" style="position:absolute">
    <defs>
      <symbol id="icon-phone" viewBox="0 0 10 10">
        <circle cx="5" cy="5" r="4.4" fill="none" stroke="currentColor" stroke-width=".8"/>
        <path d="M3.4 2.8c.3-.3.6-.3.8 0l.5.7c.2.3.1.5-.1.7l-.3.2c.3.7.8 1.2 1.5 1.5l.2-.3c.2-.2.4-.3.7-.1l.7.5c.3.2.3.5 0 .8-.5.5-1.2.6-2 .1-1-.6-1.8-1.4-2.3-2.4-.3-.7-.2-1.3.3-1.7z" fill="currentColor"/>
      </symbol>
      <symbol id="icon-mail" viewBox="0 0 10 10">
        <circle cx="5" cy="5" r="4.4" fill="currentColor"/>
        <rect x="2.6" y="3.4" width="4.8" height="3.2" fill="#f1f1f1"/>
      </symbol>
      <symbol id="icon-web" viewBox="0 0 10 10">
        <circle cx="5" cy="5" r="4.4" fill="currentColor"/>
        <circle cx="5" cy="5" r="2.2" fill="none" stroke="#f1f1f1" stroke-width=".7"/>
      </symbol>
    </defs>
  </svg>

  <!-- letterhead -->
  <div class="piece backing-sheet" role="img" aria-label="Grey second sheet with soft wave texture"></div>
  <div class="piece letterhead">
    <div class="wordmark"><span class="name">Tamarind Crest</span><span class="sub">Hotel</span></div>
    <div class="contact-block">
      <div>Governor Lualhati Avenue corner</div>
      <div>Pindang St, Cebu City</div>
      <div>Cebu, 6000, <b>Philippines</b></div>
      <div class="phones">
        <div class="phone-row">+63324805273 <svg><use href="#icon-phone"/></svg></div>
        <div class="phone-row">+639176084926 <svg><use href="#icon-phone"/></svg></div>
        <div class="phone-row">+639185550247 <svg><use href="#icon-phone"/></svg></div>
      </div>
    </div>
    <div class="letter-body">
      <p>Dear Friend,</p>
      <p>Lorem ipsum dolor sit amet, consectetur adipisicing elit, sed do eiusmod tempor incididunt ut labore et dolore magna aliqua. Ut enim ad minim veniam, quis nostrud exercitation ullamco laboris nisi ut aliquip ex ea commodo consequat. Duis aute irure dolor in reprehenderit in voluptate vet nulla pariatur. Excepted est laborum.</p>
      <p>Lorem ipsum dolor sit amet, consectetur adipisicing elit, sed do eiusmod tempor incididunt ut labore et dolore magna aliqua. Ut enim ad minim veniam, quis nostrud exercitation ullamco laboris nisi ut aliquip ex ea commodo consequat. Duis t anim id est laborum. Lorem ipsum dolor sit amet, consectetur adipisimodo consequat.</p>
      <p>Excepteur sint occaecat cupidatat non proident, sunt in culpa qui officia deserunt mollit anim id est laborum. Lorem ipsum dolor sit amet, consectetur adipisicing elit, sed do eiusmod oris nisi ut aliquip ex ea commodo consequat. Duis aute irure dolor in reprehenderit in voluptate velit esse cillum dolore eu fugiat nulla pari.</p>
      <p>Lorem ipsum dolor sit amet, consectetur adipisicing elit, sed do eiusmod tempor incididunt ut labore et dolore magna aliqua. Ut enim adonsequat. Duis aute irure dolor in reprehenderit in voluptate velit esse cillum dolore eu fugiat nulla pariatur.</p>
      <p>Best regards,</p>
      <p class="signer">Rafael Dizon</p>
      <svg class="signature-line" viewBox="0 0 120 14"><path d="M2 10c6-6 8-2 10 0s6-4 9 0 4 1 8-1 6 2 12-2 10 3 14 2 40 1 60 2" fill="none" stroke="#777" stroke-width=".8"/></svg>
    </div>
    <div class="letter-footer">reservations@tamarindcresthotel.example<span>|</span>www.tamarindcresthotel.example</div>
  </div>

  <!-- envelopes -->
  <div class="piece envelope-front">
    <svg class="flap" viewBox="0 0 434 82" preserveAspectRatio="none" role="img" aria-label="Taupe envelope flap with fine wave texture">
      <polygon points="0,0 434,0 434,66 217,82 0,66" fill="var(--taupe)"/>
    </svg>
    <div class="wordmark"><span class="name">Tamarind Crest</span><span class="sub">Hotel</span></div>
  </div>
  <div class="piece envelope-back">
    <div class="contact-left">
      <div>Governor Lualhati Avenue corner</div>
      <div>Pindang St, Cebu City</div>
      <div>Cebu, 6000, <b>Philippines</b></div>
      <div class="phones">
        <div class="phone-row"><svg><use href="#icon-phone"/></svg> +63324805273</div>
        <div class="phone-row"><svg><use href="#icon-phone"/></svg> +639176084926</div>
        <div class="phone-row"><svg><use href="#icon-phone"/></svg> +639185550247</div>
      </div>
    </div>
    <div class="contact-right">
      <div>reservations@tamarindcresthotel.example</div>
      <div>www.tamarindcresthotel.example</div>
    </div>
  </div>

  <!-- business cards -->
  <div class="piece card-front">
    <div class="holder">Rafael DIZON</div>
    <div class="role">Managing Director</div>
    <div class="rule"></div>
    <div class="mini-mark">Tamarind<br>Crest</div>
    <div class="lines">
      <div class="phone-row"><svg><use href="#icon-phone"/></svg> +63324805273</div>
      <div class="phone-row"><svg><use href="#icon-phone"/></svg> +639176084926</div>
      <div class="phone-row"><svg><use href="#icon-phone"/></svg> +639185550247</div>
      <div class="phone-row"><svg><use href="#icon-mail"/></svg> rafael@tamarindcresthotel.example</div>
      <div class="phone-row"><svg><use href="#icon-web"/></svg> www.tamarindcresthotel.example</div>
    </div>
    <div class="address">
      <div>Governor Lualhati Ave</div>
      <div>corner Pindang St</div>
      <div>Cebu City</div>
      <div>Cebu, 6000, <b>Philippines</b></div>
    </div>
  </div>
  <div class="piece card-back">
    <div class="wordmark"><span class="name">Tamarind Crest</span><span class="sub">Hotel</span></div>
  </div>

  <!-- notebook -->
  <div class="piece notebook">
    <div class="spine"></div>
    <div class="strap"></div>
    <div class="wordmark"><span class="name">Tamarind Crest</span><span class="sub">Hotel</span></div>
  </div>

</div>
</body>
</html>
```